Chocoloate confectionery company requires vibrant Packaging Design for a mini chocolate bar

- Need a packaging design for a new product; a chocolate mini-bar.
- Our corporate colors of brown and pink should be included in design.
- The chocolate weighs 20grams and measures 8 cm length x 5 cm width x 1 cm depth
- It will be covered in gold foil and wrapped in a paper sleeve.
- The paper sleeve measures 13.5 cm length x 7.5 cm width
- The paper sleeve can then be sectioned into 3 equal areas
- The packaging design is required on middle section of the sleeve.
- The ingredients, company details, barcode and disclaimer etc will be on the right section
- The left section of the sleeve may be left blank

PLEASE SEE SAMPLE PICTURES PER ATTACHED

Target Market(s)

Everyday shoppers (e.g. Moms, Dads, kids, teens, students)

Industry/Entity Type

It Company

Requirements
Must have
• Brown and pink colors (as per business card attached)
Name of mini chocolate bar is Mallow Nib. This must appear on middle section of paper sleeve

```html
<!DOCTYPE html>
<html lang="en">
<head>
<meta charset="UTF-8">
<title>Mallow Nib – Mini Bar Sleeve</title>
<link href="https://fonts.googleapis.com/css2?family=Roboto+Condensed:wght@400;700;900&display=swap" rel="stylesheet">
<style>
  :root {
    --canvas: #ffffff;
    --panel-line: #9a9a9a;
    --brand-pink: #e3007d;
    --pink-light: #f8d3df;
    --pink-mid: #f1a9c2;
    --pink-deep: #e66b96;
    --choc-dark: #3e1509;
    --choc-mid: #6a2a12;
    --ink: #111111;
    --white: #ffffff;
  }
  * { margin: 0; padding: 0; box-sizing: border-box; }
  html, body {
    width: 1200px; height: 717px; overflow: hidden;
    background: var(--canvas);
    font-family: "Roboto Condensed", "Arial Narrow", sans-serif;
    color: var(--ink);
  }
  .sleeve { position: relative; width: 1200px; height: 717px; }
  .panel { position: absolute; top: 52px; height: 608px; }

  /* left section */
  .panel-left { left: 36px; width: 364px; border: 1px solid var(--panel-line); }
  .panel-left .note {
    position: absolute; left: 111px; top: 294px;
    font-size: 20px; font-weight: 700;
  }

  /* middle section */
  .panel-front { left: 404px; width: 364px; overflow: hidden; }
  .choc-backdrop {
    position: absolute; inset: 0;
    background: linear-gradient(180deg, var(--choc-mid) 0%, var(--choc-dark) 50%, var(--choc-mid) 100%);
  }
  .name-band {
    position: absolute; left: 0; right: 0; top: 176px; height: 143px;
    background: var(--white);
  }
  .name-plate {
    position: absolute; left: 5px; right: 6px; top: 183px; height: 77px;
    margin-top: 0;
    background: var(--brand-pink);
    display: flex; align-items: center; justify-content: center;
  }
  .name-plate { height: 77px; top: 183px; }
  .name-plate span {
    color: var(--white); font-weight: 900; font-size: 56px; letter-spacing: 1px; line-height: 1;
  }
  .weight {
    position: absolute; left: 14px; bottom: 8px;
    color: var(--white); font-weight: 700; font-size: 20px;
  }

  /* right section */
  .panel-info { left: 774px; width: 370px; overflow: hidden; }
  .pattern {
    position: absolute; inset: 0;
    background: linear-gradient(165deg, var(--pink-light) 0%, var(--pink-light) 50%, var(--pink-mid) 78%, var(--pink-deep) 100%);
  }
  .tag {
    position: absolute; left: 170px; top: 14px; width: 194px; height: 46px;
    background: var(--brand-pink);
    display: flex; align-items: center; justify-content: center;
    color: var(--white); font-weight: 900; font-size: 24px; letter-spacing: .5px;
  }
  .info-head {
    position: absolute; left: 29px;
    font-size: 26px; font-weight: 700; line-height: 30px; white-space: nowrap;
  }
  .info-text {
    position: absolute; left: 29px;
    font-size: 18.5px; font-weight: 400; line-height: 33px; white-space: nowrap;
  }
  .ingredients-head { top: 84px; }
  .ingredients-text { top: 118px; }
  .allergens-head { top: 267px; }
  .allergens-text { top: 300px; }
  .origin-head { top: 393px; font-size: 25px; }
  .origin-text { top: 423px; }
  .code-box {
    position: absolute; left: 32px; top: 518px; width: 306px; height: 73px;
    background: var(--white);
  }
</style>
</head>
<body>
  <main class="sleeve">
    <section class="panel panel-left">
      <span class="note">blank</span>
    </section>

    <section class="panel panel-front">
      <div class="choc-backdrop" role="img" aria-label="Flowing melted chocolate photograph"></div>
      <div class="name-band"></div>
      <div class="name-plate"><span>MALLOW NIB</span></div>
      <span class="weight">20 GRAMS</span>
    </section>

    <section class="panel panel-info">
      <div class="pattern" role="img" aria-label="Pink geometric triangle pattern"></div>
      <div class="tag">MALLOW NIB</div>

      <h2 class="info-head ingredients-head">INGREDIENTS:</h2>
      <p class="info-text ingredients-text">Sugar, Soya,Hydrogenated Vegetable Fats<br>(Palm Kernel), Maltodextrin, Low-Fat Cocoa<br>Powder, Whey Powder (Milk), Lecithin,<br>Flavouring, Emulsifier</p>

      <h2 class="info-head allergens-head">ALLERGINS:</h2>
      <p class="info-text allergens-text">Contains Cow's Milk, Soya Beans. May<br>contain Tree Nuts.</p>

      <h2 class="info-head origin-head">HOMEMADE IN ZIMBABWE</h2>
      <p class="info-text origin-text">XYZ contact details to come</p>

      <div class="code-box"></div>
    </section>
  </main>
</body>
</html>
```